We need a web design for our business in which we provide complete network packages.

Hello Designers!

First, we’d like to make clear that rather than simple web design contents. We want someone that can help design our visual branding, help us communicate a sentiment. And we are willing to pay for that.

Who are we?

We are Harbor Lumen. Our company is based in Rotterdam, the Netherlands. We are providing a unique full-service concept for (wireless) communication networks within small to mid-range businesses. This means we will not only provide the hardware needed for a fast and secure network within a company, but will also install, optimize, support and maintain it. 

Harbor Lumen is a new brand of a company called Vector Lumen which has over 15 years of experience in the market of customer service and support. Harbor Lumen is the first satellite of more to come. Like Gear Lumen and others Planets, all have a focus on full service solutions.

Harbor Lumen has an experienced support center from which we can monitor our clients network in real time. Our clients don’t have to worry about anything, if something is not working correctly, we will fix it pro actively. Our clients range from education and training facilities, catering, industry, logistics, health care, consultancy agencies and high end consumers. 

In an overview all Unique Selling Points of Harbor Lumen:
• Professional service, both on location and remote!
• Direct clear price indication via our unique business configuration wizard
• A specific and complete quotation after a personal intake, within two days.
• Backed by a professional call center open 12 hours a day and open on Saturdays as well.
• Backed by a professional repair center with more than 15 years of experience.
• Installation and configuration included.
• Optimization included within the first three months powered by AI and machine learning.
• Real time remote maintenance. Quality control, security and interference.

Logo
For our business we need a logo. The logo needs to tell what we stand for and what we do. It will be used in both online and offline communication to our customers. Mainly e-mail and digital forms. As Harbor Lumen is one of the branches within our company we would like the logo to be part of a series in the future, which should be recognizable as part of a group of websites/brands.

Website
For our business we need a website.  The website needs a story and matching design and this is where you come in. The main focus of this website is to provide information, but more importantly to guide the user to our special quotation business configuration wizard. This business configuration wizard allows users to fill in information about their business and wish requirements, at which they will receive a real time price indication on completion. 

Configuration wizard
This business configuration wizard is developed separately by our own development team but should be part of the website in look and feel.. Our development team will develop the business configuration wizard and embed it in the website. 
The setup of the website should be focused on leading all visitors to the business configuration wizard which we create our quality leads. The website will inform the possible customers/leads on the unique selling points and then remind the customer to use the business configuration wizard to get a direct price indication. 

For the website and logo we need the whole package, the design you are creating needs to have returning elements like fonts, icons, color use,  images, maybe even characters etc. You name it! 
There needs to be a common thread in the design so we can reuse elements in, for example, the email templates, the work order or receipt we give to our customers (we may contact the winner of the contest to design these for us as well!). 

The layout needs to be complete. We want something modern. A one page design that is bright and colorful with collapsing area’s to show more information. 

Website wishes and requirements
The process:
The main function of our website, besides giving a clear indication what we do, will be to guide the user to our ‘business configuration wizard’. 

Website functionality:
Our website will be our main form of communication. We need a main/front page designed in a long single scrolling page style. Users can click on buttons to view more information. Information that was hidden before. We have included our own temporary mock ups to give you an idea of the flow we desire for the website. The titles and headers in these mock ups are in Dutch but we will translate this in the description below. These mock ups are just that, an idea about the visual presentation. You are free to implement your own design, fonts, icons, pictures etc.

The page will have 6 different areas (beside the top ‘hero’ part) and a final 7th area which is the “end page” and is a big business configuration wizard promotion.In each area you are pointed towards the business configuration wizard but if you scroll all the way down you will end up with this 7th area which is all about the wizard. However these 6 areas will need to be ‘expandable/collapsible’, meaning the user can click a “read more” button at which the element will expand to show extra information beneath it. The user can then collapse this element again by closing the part that just opened.

1. Top/Hero - Customers will be able to configure their own price indication through our wizard. So there will need to be a prominent button at the top of our main page and on the 7th area that will bring the customer to this wizard/application. This will need to be a focus throughout the whole website, meaning this button is a returning element. Furthermore the top needs two menus. One for navigating the main page itself, the other one is for switching between the different industry ‘flavors’ (Education, Logistics, Health Care etc). The idea is that the photos and text on the website will change depending on the industry picked. The design and layout remains the same however. The mock ups are based on ‘education’ and another based on logistics.

2. Real time Maintenance (Beheer) – This will be a collapsible component. It will provide a brief description of our maintenance service. The ‘configure now!’ button will need to be displayed in this area as well. This component is collapsible, meaning the user can click on a ‘Read more’ (Dutch: lees meer) button at which the element will open up to show extra information (2.1).
2.1 The extra information that can be collapsed by clicking the ‘X’ button. The headers on this page read “Carefree real time maintenance”, “Certified team of administrators”, “High service level”, “Defects immediately detected”, “Continuous remote maintenance”.

3.  Service range (Bereik) - This will be a collapsible component. It will provide a brief description of how we provide for enough wifi range within a building or company. The ‘configure now!’ button will need to be displayed in this area as well. This component is collapsible, meaning the user can click on a ‘Read more’ (Dutch: lees meer) button at which the element will open up to show extra information (3.1).
3.1 The extra information that can be collapsed by clicking the ‘X’ button. The headers on this page read “Enough range everywhere”, “Machine learning for maximum range”, “Different types of access points”, “Beamforming & Mu-MiMo”, “Multiple locations connected”.

4. Speed (Snelheid) -  This is the only component that needs to collapse twice. It will provide a brief description of how we will guarantee the fastest network speed possible. The ‘configure now!’ button will need to be displayed in this area as well. This component is collapsible, meaning the user can click on a ‘Read more’ (Dutch: lees meer) button at which the element will open up to show extra information (4.1).
4.1 The extra information that can be collapsed by clicking the ‘X’ button. The headers on this page read “Band steering, “Airtime fairness”, “Load balancing”. The user will be able to open up another element to show even more information (4.2).
4.2 This will mainly show the diagrams shown in the mock ups. It will provide extra information on what is meant by “Airtime fairness” and “Load balancing”.

5.  Manageable Costs (Beheersbare kosten) - This will be a collapsible component. It will provide a brief description of how users can manage their own costs. The ‘configure now!’ button will need to be displayed in this area as well. This component is collapsible, meaning the user can click on a ‘Read more’ (Dutch: lees meer) button at which the element will open up to show extra information (5.1).
5.1 The extra information that can be collapsed by clicking the ‘X’ button. The headers on this page read “Manageable costs”, “Upfront insight in predicated costs”, “Best price/quality ratio”, “10 years of warranty”, “High availability”.

6.  Protected and secure (Beschermd en veilig) -  This will be a collapsible component. It will provide a brief description of our protection and security guaranties. The ‘configure now!’ button will need to be displayed in this area as well. This component is collapsible, meaning the user can click on a ‘Read more’ (Dutch: lees meer) button at which the element will open up to show extra information (6.1).
6.1 The extra information that can be collapsed by clicking the ‘X’ button. The headers on this page read “Protected and Secure”, “Protected by Kelvo”, “Fire resistant and dust free”, “Managed and maintained in the Netherlands”.

7. Extras (Extra’s) - This will be a collapsible component. It will provide a brief description of additional options which our solution can provide. The ‘configure now!’ button will need to be displayed in this area as well. This component is collapsible, meaning the user can click on a ‘Read more’ (Dutch: lees meer) button at which the element will open up to show extra information (7.1).
7.1 The extra information that can be collapsed by clicking the ‘X’ button. The headers on this page read “Connection with portals like Chatloom”, “Everything in one cable”, “Cloud ready”, “Ready for even more?”.

8. unique business configuration wizard - This is the final page to (once again!) push the visitor to the ‘configure now!’ button showing some reasons to click right now.

For now, we need a logo and a website designed. We would also like a design for the configuration wizard in the same style as the website.

What we'd like:
- A modern professional, but fun, appearance
- Elements like icons to have a flat design.
- Website can be used for the different industry flavors (for example, our mockups are geared towards clients in the education sector, but we can simply swap some of the photos and content to reflect the health care sector).
- Keep in mind that the website will need to be responsive when designing!
- Create a fun and trustworthy feeling.

We will be able to provide stock photographs if necessary!

```html
<!DOCTYPE html>
<html lang="nl">
<head>
<meta charset="utf-8">
<title>Harbor Lumen – Beheerde Draadloze Netwerken</title>
<link rel="stylesheet" href="https://fonts.googleapis.com/css2?family=Rubik:wght@400;500;600&family=Lato:wght@400;700&display=swap">
<style>
  :root{
    --navy:#23386e;
    --navy-deep:#1b2d5c;
    --orange:#f58634;
    --orange-dark:#f27a20;
    --orange-soft:#fb9a4b;
    --mist:#f4f5f9;
    --ink:#5b6277;
    --white:#ffffff;
  }
  *{margin:0;padding:0;box-sizing:border-box}
  html,body{width:1200px;height:4839px;overflow:hidden}
  body{position:relative;background:var(--white);font-family:'Lato',sans-serif;color:var(--ink)}
  .abs{position:absolute}
  .heading{font-family:'Rubik',sans-serif;font-weight:500;font-size:46px;line-height:58px;color:var(--navy);letter-spacing:1px;text-transform:uppercase}
  .heading .accent{color:var(--orange)}
  .rule{position:absolute;width:56px;height:3px;background:var(--orange)}
  .copy{position:absolute;font-size:13px;line-height:19.5px;color:var(--ink)}
  .btn{position:absolute;display:flex;align-items:center;justify-content:center;background:var(--orange);color:var(--white);font-family:'Lato',sans-serif;font-size:14px;border-radius:5px}
  .photo{position:absolute}
  .dots{position:absolute;background:rgba(245,134,52,.12)}
  .panel{position:absolute;background:var(--mist)}

  /* header */
  .brand{left:88px;top:42px;font-family:'Rubik',sans-serif;font-weight:600;font-size:21px;color:var(--white);letter-spacing:1px}
  .menu-toggle{left:688px;top:42px;width:32px;height:24px}
  .login{left:836px;top:45px;font-size:13px;color:var(--navy);display:flex;align-items:center;gap:5px}
  .divider{left:905px;top:38px;width:1px;height:32px;background:#e2e4ea}
  .apply{left:926px;top:36px;width:118px;height:34px}
  .lang{left:1060px;top:36px;width:36px;height:36px;border:1.5px solid var(--navy);border-radius:50%;font-size:10px;color:var(--navy);display:flex;align-items:center;justify-content:center;font-weight:700}
  .lang-caret{left:1100px;top:48px}

  /* hero */
  .hero-sub{left:90px;top:306px;font-size:24px;color:var(--white)}
  .hero-title{left:88px;top:342px;font-family:'Rubik',sans-serif;font-weight:500;font-size:66px;line-height:74px;color:var(--white);letter-spacing:1.5px}
  .hero-cta{left:90px;top:505px;width:140px;height:36px}

  /* closing */
  .closing-title{left:0;width:1200px;top:4416px;text-align:center;font-family:'Rubik',sans-serif;font-weight:500;font-size:48px;color:var(--white);letter-spacing:1px}
  .closing-sub{top:4512px;font-family:'Rubik',sans-serif;font-weight:500;font-size:21px;color:var(--white)}
  .closing-line{top:4595px;height:1px;background:rgba(255,255,255,.3)}
  .closing-cta{left:530px;top:4578px;width:140px;height:34px}
  .sector-nav{left:148px;top:4672px;width:904px;display:flex;justify-content:space-between;font-family:'Rubik',sans-serif;font-size:16px;color:var(--white)}
  .copyright{left:0;width:1200px;top:4796px;text-align:center;font-family:'Rubik',sans-serif;font-size:14px;color:var(--white);letter-spacing:.5px}
</style>
</head>
<body>

<!-- HERO -->
<svg class="abs" style="left:0;top:0" width="1200" height="770" role="img" aria-label="Studenten in een klaslokaal onder een donkerblauwe kleurlaag">
  <defs>
    <linearGradient id="heroTone" x1="0" y1="0" x2="1" y2="1">
      <stop offset="0" stop-color="#2c4580"/>
      <stop offset="1" stop-color="#1c2f60"/>
    </linearGradient>
  </defs>
  <path d="M0 0 H762 C772 330 560 720 0 766 Z" fill="url(#heroTone)"/>
</svg>

<header>
  <div class="abs brand">HARBOR LUMEN</div>
  <svg class="abs menu-toggle" viewBox="0 0 32 24"><rect y="2" width="30" height="3" fill="#fff"/><rect y="10" width="30" height="3" fill="#fff"/><rect y="18" width="30" height="3" fill="#fff"/></svg>
  <div class="abs login"><svg width="10" height="11" viewBox="0 0 10 11"><circle cx="5" cy="3" r="2.6" fill="#23386e"/><path d="M0 11 C0 6 10 6 10 11Z" fill="#23386e"/></svg>Login</div>
  <div class="abs divider"></div>
  <div class="btn apply">Apply Now</div>
  <div class="abs lang">ENG</div>
  <svg class="abs lang-caret" width="8" height="6" viewBox="0 0 8 6"><path d="M1 1 L4 4 L7 1" stroke="#23386e" stroke-width="1.5" fill="none"/></svg>
</header>

<section class="hero">
  <div class="abs hero-sub">Beheerde Draadloze Netwerken</div>
  <h1 class="abs hero-title">VOORHET<br>ONDERWIJIS</h1>
  <div class="btn hero-cta">Configureer Nu!</div>
  <div class="photo" style="left:539px;top:173px;width:661px;height:526px;background:linear-gradient(135deg,#c9a884,#e7d3bd 50%,#7a6048);box-shadow:0 10px 30px rgba(0,0,0,.12)" role="img" aria-label="Drie lachende studenten rond een laptop"></div>
</section>

<!-- 1 BEHEER -->
<section class="feature">
  <div class="dots" style="left:8px;top:930px;width:16px;height:244px" role="img" aria-label="Decoratief stippenpatroon"></div>
  <div class="photo" style="left:6px;top:890px;width:614px;height:321px;background:linear-gradient(180deg,#2a2d33,#1a1c20 85%,#b9bcc2)" role="img" aria-label="Laptop met netwerkbeheer-dashboard"></div>
  <h2 class="abs heading" style="left:618px;top:916px"><span class="accent">Zorgeloos</span><br>Realtime beheer</h2>
  <div class="rule" style="left:618px;top:1045px"></div>
  <p class="copy" style="left:618px;top:1071px;width:496px">Lorem Ipsum has been the industry's standard dummy text ever since the 1500s when an unknown printer took a galley of type and a type specimen book It has survived not only five centuriesLorem Ipsum has been the indus-try's standard dummy text ever since the 1500s when an unknown printer took a galley of type.</p>
</section>

<!-- 2 BEREIK -->
<section class="feature">
  <div class="panel" style="left:0;top:1352px;width:1200px;height:573px"></div>
  <h2 class="abs heading" style="left:94px;top:1504px"><span class="accent">Overal</span><br>voldoende bereik</h2>
  <div class="rule" style="left:94px;top:1633px"></div>
  <p class="copy" style="left:94px;top:1659px;width:494px">Lorem Ipsum has been the industry's standard dummy text ever since the 1500s when an unknown printer took a galley of type and a type specimen book It has survived not only five centuriesLorem Ipsum has been the indus-try's standard dummy text ever since the 1500s when an unknown printer took a galley of type.</p>
  <div class="photo" style="left:582px;top:1478px;width:614px;height:321px;background:linear-gradient(180deg,#2a2d33,#8b8f8a 20%,#c7a35c 70%,#1a1c20 92%,#b9bcc2)" role="img" aria-label="Laptop met beeld van een leerling die haar hand opsteekt in de klas"></div>
  <div class="dots" style="left:1160px;top:1520px;width:34px;height:236px" role="img" aria-label="Decoratief stippenpatroon"></div>
</section>

<!-- 3 SNELHEID -->
<section class="feature">
  <div class="panel" style="left:0;top:2021px;width:470px;height:383px"></div>
  <div class="photo" style="left:62px;top:2092px;width:486px;height:270px;background:linear-gradient(110deg,#9fb6c9,#d9cfc2 55%,#c9a27e)" role="img" aria-label="Lachend meisje achter een computer met een wereldkaart"></div>
  <h2 class="abs heading" style="left:618px;top:2098px"><span class="accent">Snelheid</span><br>altijd voldoende...</h2>
  <div class="rule" style="left:618px;top:2230px"></div>
  <p class="copy" style="left:618px;top:2255px;width:496px">Lorem Ipsum has been the industry's standard dummy text ever since the 1500s when an unknown printer took a galley of type and a type specimen book It has survived not only five centuriesLorem Ipsum has been the indus-try's standard dummy text ever since the 1500s when an unknown printer took a galley of type.</p>
  <div class="dots" style="left:1162px;top:2112px;width:32px;height:240px" role="img" aria-label="Decoratief stippenpatroon"></div>
</section>

<!-- 4 KOSTEN -->
<section class="feature">
  <div class="photo" style="left:0;top:2528px;width:1200px;height:571px;background:linear-gradient(100deg,var(--orange-soft),var(--orange) 60%)" role="img" aria-label="Klaslokaal onder een oranje kleurlaag"></div>
  <div class="abs" style="left:1020px;top:2528px;width:180px;height:571px;background:var(--orange-dark)"></div>
  <div class="dots" style="left:6px;top:2695px;width:30px;height:235px;background:rgba(255,255,255,.15)" role="img" aria-label="Decoratief stippenpatroon"></div>
  <h2 class="abs heading" style="left:94px;top:2708px;color:var(--white)">Beheersbare kosten</h2>
  <div class="rule" style="left:94px;top:2788px;background:var(--white)"></div>
  <p class="copy" style="left:94px;top:2812px;width:540px;color:var(--white)">Lorem Ipsum has been the industry's standard dummy text ever since the 1500s when an unknown printer took a galley of type and a type specimen book It has sur-vived not only five centuriesLorem Ipsum has been the industry's standard dummy text ever since the 1500s when an unknown printer took a galley of type and a type specimen book It has survived not only five centuries</p>
  <div class="photo" style="left:715px;top:2638px;width:485px;height:336px;background:rgba(255,255,255,.85)"></div>
  <div class="photo" style="left:727px;top:2650px;width:473px;height:312px;background:linear-gradient(120deg,#d8d3cb,#a8876a 55%,#e5e3df)" role="img" aria-label="Kinderen in de klas rond een tablet met hun docent"></div>
</section>

<!-- 5 VEILIG -->
<section class="feature">
  <div class="panel" style="left:28px;top:3217px;width:485px;height:383px"></div>
  <div class="photo" style="left:0;top:3208px;width:475px;height:357px;background:linear-gradient(110deg,#c99524,#b8a894 45%,#ece8e2)" role="img" aria-label="Student kijkt over een laptop naar een collega"></div>
  <h2 class="abs heading" style="left:565px;top:3307px">Beschermd en veilig</h2>
  <div class="rule" style="left:565px;top:3389px"></div>
  <p class="copy" style="left:565px;top:3413px;width:496px">Lorem Ipsum has been the industry's standard dummy text ever since the 1500s when an unknown printer took a galley of type and a type specimen book It has survived not only five centuriesLorem Ipsum has been the indus-try's standard dummy text ever since the 1500s when an unknown printer took a galley of type.</p>
  <div class="dots" style="left:1154px;top:3296px;width:40px;height:236px" role="img" aria-label="Decoratief stippenpatroon"></div>
</section>

<!-- 6 EXTRA'S -->
<section class="feature">
  <div class="dots" style="left:6px;top:3822px;width:36px;height:235px" role="img" aria-label="Decoratief stippenpatroon"></div>
  <h2 class="abs heading" style="left:94px;top:3839px">Nogmeer waarde</h2>
  <div class="rule" style="left:94px;top:3920px"></div>
  <p class="copy" style="left:94px;top:3944px;width:496px">Lorem Ipsum has been the industry's standard dummy text ever since the 1500s when an unknown printer took a galley of type and a type specimen book It has survived not only five centuriesLorem Ipsum has been the indus-try's standard dummy text ever since the 1500s when an unknown printer took a galley of type.</p>
  <div class="panel" style="left:693px;top:3703px;width:484px;height:429px"></div>
  <div class="photo" style="left:729px;top:3750px;width:424px;height:350px;background:linear-gradient(160deg,#2f5a45,#4e7a5e 45%,#a07a55 80%,#6b4a32)" role="img" aria-label="Boeken en een pennenbak met kleurpotloden voor een schoolbord"></div>
</section>

<!-- CONFIGURATOR -->
<footer>
  <svg class="abs" style="left:0;top:4255px" width="1200" height="584" role="img" aria-label="Klaslokaal onder een donkerblauwe kleurlaag">
    <path d="M0 122 C300 0 900 0 1200 122 V584 H0 Z" fill="var(--navy)"/>
  </svg>
  <h2 class="abs closing-title">GELIJK EEN OPGAVE VAN KOSTEN?</h2>
  <div class="abs closing-sub" style="left:150px">VRAGEN OF MEER INFORMATIE?</div>
  <div class="abs closing-sub" style="left:617px">GEBRUIK ONZE UNIEKE CONFIGURATOR!</div>
  <div class="abs closing-line" style="left:150px;width:322px"></div>
  <div class="abs closing-line" style="left:724px;width:326px"></div>
  <div class="btn closing-cta">Configureer Nu!</div>
  <nav class="abs sector-nav">
    <span>ONDERWIJS</span><span>LOGISTIEK</span><span>INDUSTRIE</span><span>KANTOOR</span><span>GEZONDHEIDSZORG</span><span>RESTAURANT</span><span>VILLA</span>
  </nav>
  <div class="abs copyright">COPYRIGHT 2020 - ALLRIGHT RESERVED.</div>
</footer>

</body>
</html>
```